Business Card Design

we are a brand new cable TV network devoted to self improvement and leading a better life called FLOURIVO TV.I have a logo. We have 3 executives that need cards.I want it to be a heavy stock card: professional but showing our creative nature

Industry/Entity Type

Business

Contact Information for Business Card

CLAUDIA SAENZ AMLIECEO350 San Juan DrPonte Vedra Beach FL 32082904-473-5953

```html
<!DOCTYPE html>
<html lang="en">
<head>
<meta charset="utf-8">
<title>FLOURIVO TV – Business Card</title>
<link rel="stylesheet" href="https://fonts.googleapis.com/css2?family=Crimson+Text:wght@400;600&display=swap">
<style>
  :root {
    --bg: #ecebe8;
    --card: #ffffff;
    --ink: #2b2b2d;
    --ink-soft: #4a4a4c;
    --red: #d71e28;
    --black: #1f1e20;
  }
  * { margin: 0; padding: 0; box-sizing: border-box; }
  html, body {
    width: 1200px; height: 902px; overflow: hidden;
    background: var(--bg);
    font-family: "Crimson Text", Georgia, serif;
  }
  .canvas {
    position: relative; width: 1200px; height: 902px;
    display: flex; align-items: center; justify-content: center;
  }
  .card {
    position: relative; width: 1000px; height: 572px;
    background: var(--card);
    box-shadow: 0 14px 40px rgba(0,0,0,.18);
    overflow: hidden;
  }
  .card__edge { position: absolute; inset: 0; width: 100%; height: 100%; }
  .brand {
    position: absolute; left: 90px; top: 262px;
    display: flex; align-items: center; gap: 16px;
    max-width: 430px; white-space: nowrap;
  }
  .brand__mark { width: 18px; height: 18px; background: var(--red); flex: none; }
  .brand__name {
    font-weight: 600; font-size: 56px; letter-spacing: 0;
    color: var(--ink); line-height: 1;
  }
  .divider {
    position: absolute; left: 545px; top: 150px; width: 1.5px; height: 190px;
    background: linear-gradient(to bottom, var(--red), rgba(215,30,40,.15));
  }
  .contact { position: absolute; left: 575px; top: 78px; color: var(--ink-soft); }
  .contact__name { font-size: 30px; color: var(--red); font-weight: 600; line-height: 1.1; }
  .contact__role { font-size: 21px; margin-top: 4px; }
  .contact__address { font-size: 21px; line-height: 1.3; margin-top: 34px; padding-left: 40px; }
  .contact__list { list-style: none; margin-top: 30px; font-size: 21px; }
  .contact__item { display: flex; align-items: center; gap: 14px; padding-left: 40px; height: 34px; }
  .contact__icon { width: 18px; height: 18px; flex: none; fill: none; stroke: var(--red); stroke-width: 2; }
  .contact__icon--solid { fill: var(--red); stroke: none; }
</style>
</head>
<body>
<main class="canvas">
  <article class="card">
    <svg class="card__edge" viewBox="0 0 1000 572" preserveAspectRatio="none" aria-hidden="true">
      <polygon points="0,572 0,548 820,432 820,572" fill="var(--red)"/>
      <path d="M790,572 L800,452 C804,418 826,404 860,398 L1000,374 L1000,572 Z" fill="var(--black)"/>
    </svg>

    <div class="brand">
      <span class="brand__mark"></span>
      <span class="brand__name">FLOURIVO TV</span>
    </div>

    <div class="divider"></div>

    <section class="contact">
      <h1 class="contact__name">Mirella Okafor Dunst</h1>
      <p class="contact__role">CEO</p>
      <p class="contact__address">718 Harlow Creek Dr<br>Ponte Vedra Beach FL 32097</p>
      <ul class="contact__list">
        <li class="contact__item">
          <svg class="contact__icon contact__icon--solid" viewBox="0 0 24 24"><path d="M6.6 10.8a15.1 15.1 0 0 0 6.6 6.6l2.2-2.2c.3-.3.7-.4 1-.2 1.1.4 2.3.6 3.6.6.6 0 1 .4 1 1V20c0 .6-.4 1-1 1A17 17 0 0 1 3 4c0-.6.4-1 1-1h3.5c.6 0 1 .4 1 1 0 1.3.2 2.5.6 3.6.1.3 0 .7-.2 1z"/></svg>
          <span>904-618-2047</span>
        </li>
        <li class="contact__item">
          <svg class="contact__icon" viewBox="0 0 24 24"><circle cx="12" cy="12" r="9"/><path d="M3 12h18M12 3c3 3 3 15 0 18M12 3c-3 3-3 15 0 18"/></svg>
          <span>www.flourivotv.com</span>
        </li>
        <li class="contact__item">
          <svg class="contact__icon" viewBox="0 0 24 24"><circle cx="12" cy="12" r="4"/><path d="M16 8v5a3 3 0 0 0 5 0v-1a9 9 0 1 0-4 7.5"/></svg>
          <span>hello@flourivotv.com</span>
        </li>
      </ul>
    </section>
  </article>
</main>
</body>
</html>
```